TBrenwick Business Cards & Letterhead

I have a logo but need a design for some new business cards. We are a Design-Build Firm that specializes in the design and construction of commercial projects.
the cards need to be professional. no cartoon stuff.
i would like to have the cards in AI format so I can update the card as needed. Logo is provided.
Our Address is: 4718 Fenmoor Ct. Larkfield, Oregon 97512

```html
<!DOCTYPE html>
<html lang="en">
<head>
<meta charset="utf-8">
<title>TBrenwick Business Card</title>
<link rel="stylesheet" href="https://fonts.googleapis.com/css2?family=Lato:wght@400;700;900&display=swap">
<style>
  :root {
    --page-bg: #e9e6e4;
    --frost-light: #f2f1f3;
    --frost-mid: #c9d8e3;
    --frost-blue: #a9c0d1;
    --panel-dark: #141518;
    --panel-edge: #3d3e42;
    --name-white: #e4e4e7;
    --accent-blue: #1f5f9c;
    --icon-blue: #2a6cab;
    --text-light: #e4e4e6;
    --brand-grey: #3a3b3f;
  }
  * { margin: 0; padding: 0; box-sizing: border-box; }
  html, body {
    width: 1200px; height: 734px; overflow: hidden;
    background: var(--page-bg);
    font-family: "Lato", sans-serif;
  }
  .business-card {
    position: absolute; left: 100px; top: 81px;
    width: 1000px; height: 572px;
    border-radius: 26px; overflow: hidden;
    background: radial-gradient(ellipse at 70% 55%, var(--panel-dark) 40%, var(--panel-edge) 100%);
    box-shadow: 0 14px 40px rgba(0,0,0,.18);
  }
  .frost-panel {
    position: absolute; left: 0; top: 0; width: 574px; height: 572px;
    background: linear-gradient(135deg, var(--frost-light) 0%, var(--frost-mid) 55%, var(--frost-blue) 100%);
  }
  .brand-name {
    position: absolute; left: 0; width: 574px; top: 274px;
    text-align: center;
    font-weight: 900; font-size: 56px; letter-spacing: 1px;
    color: var(--brand-grey); line-height: 1;
  }
  .identity { position: absolute; right: 40px; top: 124px; text-align: right; }
  .person-name { font-weight: 700; font-size: 46px; color: var(--name-white); line-height: 1; letter-spacing: .3px; }
  .person-role { font-weight: 400; font-size: 27px; color: var(--accent-blue); margin-top: 8px; line-height: 1; }
  .contact-list { position: absolute; right: 42px; top: 228px; list-style: none; }
  .contact-item {
    display: flex; justify-content: flex-end; align-items: center;
    height: 35.5px; font-size: 23px; color: var(--text-light); white-space: nowrap;
  }
  .contact-item svg { width: 20px; height: 20px; margin-left: 18px; flex: none; fill: var(--icon-blue); }
  .contact-item .icon-spacer { width: 20px; margin-left: 18px; }
</style>
</head>
<body>
  <div class="business-card">
    <div class="frost-panel"></div>
    <div class="brand-name">TBRENWICK</div>

    <div class="identity">
      <div class="person-name">DANIEL HARPER</div>
      <div class="person-role">Founder &amp; CEO</div>
    </div>

    <ul class="contact-list">
      <li class="contact-item">(555) 318-2047
        <svg viewBox="0 0 24 24"><path d="M6.6 10.8a15 15 0 0 0 6.6 6.6l2.2-2.2c.3-.3.7-.4 1-.2 1.1.4 2.3.6 3.6.6.6 0 1 .4 1 1V20c0 .6-.4 1-1 1A17 17 0 0 1 3 4c0-.6.4-1 1-1h3.5c.6 0 1 .4 1 1 0 1.3.2 2.5.6 3.6.1.3 0 .7-.2 1z"/></svg>
      </li>
      <li class="contact-item">(555) 318-2048
        <svg viewBox="0 0 24 24"><path d="M7 2h10a2 2 0 0 1 2 2v16a2 2 0 0 1-2 2H7a2 2 0 0 1-2-2V4a2 2 0 0 1 2-2zm0 3v13h10V5zm5 14.2a.9.9 0 1 0 0 1.8.9.9 0 0 0 0-1.8z"/></svg>
      </li>
      <li class="contact-item">(555) 318-2049
        <svg viewBox="0 0 24 24"><path d="M7 3h10v4H7zM4 8h16a2 2 0 0 1 2 2v6h-4v5H6v-5H2v-6a2 2 0 0 1 2-2zm4 7v4h8v-4z"/></svg>
      </li>
      <li class="contact-item">office@brenwickbuild.com
        <svg viewBox="0 0 24 24"><path d="M2 5h20v14H2zm2 2v.5l8 5 8-5V7z"/></svg>
      </li>
      <li class="contact-item">www.brenwickbuild.com
        <svg viewBox="0 0 24 24"><path d="M12 2a10 10 0 1 0 0 20 10 10 0 0 0 0-20zm-1 17.9A8 8 0 0 1 4.2 10l4.8 4.8v1a2 2 0 0 0 2 2zm6.9-2.5A2 2 0 0 0 16 16h-1v-3a1 1 0 0 0-1-1H8v-2h2a1 1 0 0 0 1-1V7h2a2 2 0 0 0 2-2v-.4a8 8 0 0 1 2.9 12.8z"/></svg>
      </li>
      <li class="contact-item">4718 Fenmoor Ct. Larkfield
        <svg viewBox="0 0 24 24"><path d="M12 2a7 7 0 0 0-7 7c0 5.2 7 13 7 13s7-7.8 7-13a7 7 0 0 0-7-7zm0 9.5a2.5 2.5 0 1 1 0-5 2.5 2.5 0 0 1 0 5z"/></svg>
      </li>
      <li class="contact-item">Oregon 97512<span class="icon-spacer"></span></li>
    </ul>
  </div>
</body>
</html>
```